Business Card Design

We need a business card design for a new company. We produce and sell fully grown topiary (please Google topiary pictures if you are not familiar with Topiary).We make many different topiary designs and shapes in all sizes. Ranging from cute little table top animal sculptures such as bunnies and swans for the indoors, to big sculptures such as actual size elephants for outdoor gardens and parks. We also make topiary balls, spiral shapes and other attractive geometrical shapes for indoor and outdoor decorations. We want to see designs that reflects the playfulness and ,liveliness and cute characteristics of our products.Please find attached the logo.Thank you

Industry/Entity Type

Business

Contact Information for Business Card

Company Name : Leaf Lark
Slogan : Crafting The World In Green
Tagline: Topiary...and more
Website : www.leaflark.example

Name on Card : Yusuf Tarek Mansour
Title : Founder & CEO
email: yusuf_tarek@leaflark.example

Address : 27 El-Borsaly Street
Ground Floor,Ste.1
El-Haram,Cairo,Egypt

Office Telephone : (02) 35908176
Mobile Number : 01062719048

Requirements
Must have
• The business card must have a white background.

```html
<!DOCTYPE html>
<html lang="en">
<head>
<meta charset="utf-8">
<title>Leaf Lark – Business Card</title>
<link rel="stylesheet" href="https://fonts.googleapis.com/css2?family=Arimo:wght@400;700&family=Dancing+Script:wght@500&display=swap">
<style>
  :root {
    --backdrop: #8a6a48;
    --card: #ffffff;
    --leaf: #6c9b3a;
    --leaf-text: #76a240;
    --ink: #333333;
    --swoosh: #111111;
    --on-leaf: #ffffff;
  }
  * { margin: 0; padding: 0; box-sizing: border-box; }
  html, body {
    width: 1200px; height: 834px; overflow: hidden;
    background: var(--backdrop);
  }
  .card {
    position: absolute; left: 89px; top: 89px;
    width: 1022px; height: 664px;
    background: var(--card);
    overflow: hidden;
    font-family: "Arimo", Arial, sans-serif;
  }
  .card-base { position: absolute; inset: 0; }
  .brand {
    position: absolute; top: 110px; left: 0; width: 100%;
    display: flex; justify-content: center; align-items: center; gap: 20px;
    font-family: "Arimo", Arial, sans-serif;
    font-weight: 400;
    font-size: 80px; line-height: 1;
    color: var(--leaf);
  }
  .brand-dot {
    width: 26px; height: 26px; border-radius: 50%;
    background: var(--leaf);
  }
  .tagline {
    position: absolute; top: 256px; width: 100%; text-align: center;
    font-family: "Dancing Script", cursive;
    font-size: 32px; color: var(--leaf-text); letter-spacing: 0.5px;
  }
  .address {
    position: absolute; top: 356px; width: 100%; text-align: center;
    font-size: 25px; color: var(--ink);
  }
  .person {
    position: absolute; left: 0; width: 488px; top: 535px;
    text-align: right; color: var(--on-leaf);
  }
  .person-name { font-weight: 700; font-size: 28px; line-height: 38px; }
  .person-title { font-size: 26px; line-height: 36px; }
  .divider {
    position: absolute; left: 502px; top: 518px;
    width: 2px; height: 96px; background: var(--on-leaf);
  }
  .contacts {
    position: absolute; left: 520px; top: 490px;
    list-style: none; color: var(--on-leaf); font-size: 25px;
  }
  .contacts li {
    display: flex; align-items: center; gap: 12px;
    height: 42.5px;
  }
  .contacts svg { width: 20px; height: 20px; flex: none; }
</style>
</head>
<body>
  <main class="card">
    <svg class="card-base" viewBox="0 0 1022 664" aria-hidden="true">
      <path d="M0,585 Q470,390 1022,512 L1022,664 L0,664 Z" fill="var(--leaf)"/>
      <path d="M0,565 Q470,335 1022,496 Q470,368 0,578 Z" fill="var(--swoosh)"/>
    </svg>

    <div class="brand"><span class="brand-dot"></span>Leaf Lark</div>
    <p class="tagline">We Produce &amp; Sell Fully Grown Topiary... and more</p>
    <p class="address">27 El-Borsaly Street Ground Floor Ste.1 El-Haram,Cairo,Egypt</p>

    <div class="person">
      <div class="person-name">Yusuf Tarek Mansour</div>
      <div class="person-title">Founder &amp; CEO</div>
    </div>
    <div class="divider"></div>

    <ul class="contacts">
      <li>
        <svg viewBox="0 0 20 20" aria-hidden="true"><rect x="5" y="1" width="10" height="18" rx="2" fill="none" stroke="#fff" stroke-width="2"/><rect x="7" y="4" width="6" height="7" fill="#fff"/></svg>
        <span>01062719048</span>
      </li>
      <li>
        <svg viewBox="0 0 20 20" aria-hidden="true"><path d="M4,2 L8,2 L9,6 L7,8 Q9,12 12,13 L14,11 L18,12 L18,16 Q10,18 5,12 Q2,7 4,2 Z" fill="#fff"/></svg>
        <span>(02) 35908176</span>
      </li>
      <li>
        <svg viewBox="0 0 20 20" aria-hidden="true"><rect x="2" y="5" width="16" height="11" rx="1" fill="#fff"/><path d="M2,5 L10,11 L18,5" fill="none" stroke="var(--leaf)" stroke-width="1.5"/></svg>
        <span>yusuf_tarek@leaflark.example</span>
      </li>
      <li>
        <svg viewBox="0 0 20 20" aria-hidden="true"><circle cx="10" cy="10" r="8" fill="none" stroke="#fff" stroke-width="1.8"/><ellipse cx="10" cy="10" rx="3.5" ry="8" fill="none" stroke="#fff" stroke-width="1.5"/><path d="M2,10 H18 M3.5,6 H16.5 M3.5,14 H16.5" stroke="#fff" stroke-width="1.3"/></svg>
        <span>www.leaflark.example</span>
      </li>
    </ul>
  </main>
</body>
</html>
```